Tendril Harbor

Our product is a subscription-based website for doctors and medical practices. It allows contract-based doctors (locums) to book jobs with medical practices and to organise their own finances (invoicing, pension, etc). Also, it allows medical practices to post jobs, and book locums.

We need a website design that looks clean and professional. It should look easy-to-use and friendly, which will encourage users to sign up as they'll hopefully think using the system will also be simple and friendly.

As well as the homepage, we need a design for the logged-in view. This is very different to the website but equally important. It needs to be very functional. Much more like an application and less like a website.

PLEASE SUBMIT BOTH WEBSITE HOMEPAGE DESIGN AND APPLICATION DASHBOARD DESIGN.

The application is built and we already have a user interface (linked below) so we're not looking for a designer to decide what is on these pages - we already have that. We're ONLY asking for visual design. Please just make the content we have look good. You may move parts of the content around a small amount but the functionality is very much signed off now so it's only visual styling that we need addressed.

Please base the branding around the current logo, which can't be changed. You can get the logo as an EPS here : http://clients.brassowl.co.uk/tendrilharbor/design/logo-green.eps

Here is a link to the current design for the website, and for the application dashboard:
http://clients.brassowl.co.uk/tendrilharbor/design/

Also, here is a video we've had made which might help you with the brand:
http://quivlo.com/71825364
Updates

Just in case it isn't clear, the video (linked in the main brief) is an essential part of the website homepage.

Reason: We need to spend some time looking over these designs and might ask for a few amendments to one or two in the next few days. Thanks.

Target Market(s)

Doctors and medical practices

Industry/Entity Type

Medical

Requirements
Must have
• It must have all the features that are in the linked designs - homepage and dashboard.

```html
<!DOCTYPE html>
<html lang="en">
<head>
<meta charset="utf-8">
<title>Tendril Harbor</title>
<link href="https://fonts.googleapis.com/css2?family=Source+Sans+3:wght@400;600&display=swap" rel="stylesheet">
<style>
:root{
  --page:#f1f2f2;
  --navy:#3b6d98;
  --blue:#1a9ad6;
  --blue-dark:#1589c2;
  --green:#8bb62a;
  --green-dark:#6f9a1c;
  --ink:#555;
  --ink-soft:#777;
  --link:#2778b0;
  --white:#fff;
  --footer:#2a2a2a;
}
*{margin:0;padding:0;box-sizing:border-box}
html,body{width:774px;height:1200px;overflow:hidden}
body{position:relative;background:var(--page);font-family:"Source Sans 3",sans-serif;color:var(--ink)}
.abs{position:absolute}
.topline{left:0;top:0;width:774px;height:4px;background:var(--navy)}
.brand-dot{left:85px;top:13px;width:80px;height:80px;border-radius:50%;background:var(--navy)}
.brand-name{left:188px;top:22px;font-size:31px;line-height:31px;font-weight:600;color:var(--navy);letter-spacing:1px}
.user-name{left:582px;top:13px;font-size:11px;color:#444}
.signout{left:528px;top:45px;font-size:8px;color:#444}
.btn{display:flex;align-items:center;justify-content:center;color:var(--white);border-radius:4px;box-shadow:2px 3px 3px rgba(0,0,0,.35)}
.btn-green{background:linear-gradient(#9ccb36,var(--green-dark))}
.btn-blue{background:linear-gradient(#3fa9dc,#1f7db4)}
.dash-btn{left:576px;top:36px;width:108px;height:30px;font-size:10px}
.nav{left:0;top:100px;width:774px;height:37px;background:var(--blue);display:flex}
.nav a{position:absolute;top:0;height:37px;display:flex;align-items:center;color:var(--white);font-size:9px;text-decoration:none;padding-left:0}
.nav .active{background:var(--green);justify-content:center}
.nav .sep{position:absolute;top:0;width:1px;height:37px;background:rgba(255,255,255,.25)}
.hero{left:54px;top:146px;width:655px;height:292px;background:#f8f8f8;border:1px solid #e6e6e6}
.hero-inner{left:66px;top:156px;width:635px;height:272px;background:linear-gradient(#fff,#efefef)}
.hero-shadow{left:110px;top:434px;width:570px;height:12px;border-radius:50%;background:radial-gradient(rgba(0,0,0,.45),rgba(0,0,0,0) 70%)}
.photo-hand{left:66px;top:156px;width:98px;height:218px;background:linear-gradient(90deg,#2d2d2d,#c9a58e 70%,#e6d2c2)}
.photo-team{left:172px;top:224px;width:152px;height:96px;background:linear-gradient(#2b2b2b,#d8d8d8)}
.hero-title{left:156px;top:196px;font-size:12.5px;line-height:19px;color:var(--blue-dark)}
.hero-list{left:180px;top:257px;font-size:12px;line-height:23.3px;color:#fff;font-weight:600;text-shadow:0 0 2px #222,0 0 2px #222;list-style:none}
.read-more{left:178px;top:354px;width:96px;height:28px;font-size:11px}
.dot{top:398px;width:7px;height:7px;border-radius:50%;background:#111}
.video{left:324px;top:189px;width:360px;height:203px;border:2px solid #7d8fa0;background:radial-gradient(circle at 50% 45%,#e9f7fc,#8fcde6)}
.features{left:53px;top:473px;width:655px;height:299px;background:var(--white)}
.divider{left:376px;top:500px;width:1px;height:200px;background:linear-gradient(#fff,#ddd,#fff)}
.col-title{font-size:12px;color:#444}
.col-sub{font-size:9px;color:var(--ink-soft)}
.feat-title{font-size:9.5px;color:var(--link)}
.feat-desc{font-size:7px;line-height:11.5px;color:#666;width:200px}
.signup{width:101px;height:29px;font-size:11px}
.icon-people{width:34px;height:28px;border-radius:6px;background:linear-gradient(90deg,#d44,#e9a13a,#3c9,#37c)}
.trial{left:52px;top:783px;width:398px;height:267px;background:var(--blue-dark);color:var(--white)}
.trial-title{left:79px;top:805px;font-size:11px;color:var(--white)}
.label{font-size:8px;color:var(--white)}
.field{left:138px;width:173px;height:21px;border-radius:5px;background:linear-gradient(#e6e6e6,#fff)}
.radio{display:inline-block;width:7px;height:7px;border-radius:50%;background:#fff;border:1px solid #bbb;vertical-align:-1px;margin-right:3px}
.sign-up-big{left:326px;top:966px;width:102px;height:38px;font-size:15px}
.steps{left:463px;top:783px;width:246px;height:122px;background:var(--blue-dark)}
.step-num{left:475px;width:27px;height:27px;border-radius:50%;background:#fff;color:var(--blue-dark);font-size:13px;display:flex;align-items:center;justify-content:center}
.step-text{left:508px;font-size:11px;color:#fff}
.press{left:463px;top:914px;width:246px;height:136px;background:var(--blue-dark)}
.press-box{left:490px;width:192px;height:35px;border-radius:3px;background:#fff;display:flex;align-items:center;justify-content:center;font-size:16px;font-weight:600;color:#333}
.footer{left:0;top:1062px;width:774px;height:138px;background:var(--footer)}
.footer-title{left:72px;top:1075px;font-size:11px;color:var(--blue)}
.avatar{top:1101px;width:54px;height:53px;border-radius:6px;border:1px solid #888;background:linear-gradient(#6b5348,#c8a48a)}
.quote{top:1103px;font-size:7px;line-height:11.6px;color:#bbb;width:100px}
.person{top:1165px;font-size:8px;color:#ddd}
.more{left:412px;top:1182px;font-size:7px;color:#ccc}
.social{top:1080px;width:16px;height:16px;border-radius:2px}
.copyright{left:520px;top:1122px;width:184px;text-align:right;font-size:7px;color:#ccc}
</style>
</head>
<body>
<div class="abs topline"></div>

<header>
  <div class="abs brand-dot"></div>
  <div class="abs brand-name">TENDRIL<br>HARBOR</div>
  <div class="abs user-name">Mrs.Helena Marsh</div>
  <div class="abs signout">Signout</div>
  <div class="abs btn btn-green dash-btn">GO TO DASHBOARD</div>
</header>

<nav class="abs nav">
  <a class="active" style="left:100px;width:72px">HOME</a>
  <a style="left:190px">LOCUMS</a><span class="sep" style="left:247px"></span>
  <a style="left:270px">EMPLOYERS</a><span class="sep" style="left:333px"></span>
  <a style="left:360px">PRICING</a><span class="sep" style="left:412px"></span>
  <a style="left:435px">ABOUT US</a><span class="sep" style="left:494px"></span>
  <a style="left:518px">FAQ</a><span class="sep" style="left:558px"></span>
  <a style="left:580px">CONTACT</a>
</nav>

<section class="hero-section">
  <div class="abs hero"></div>
  <div class="abs hero-shadow"></div>
  <div class="abs hero-inner"></div>
  <div class="abs photo-hand" role="img" aria-label="Businessman in a suit reaching out for a handshake"></div>
  <div class="abs photo-team" role="img" aria-label="Row of professionals standing together"></div>
  <div class="abs hero-title">NETWORK CONNECTING<br>LOCUMS WITH EMPLOYERS</div>
  <ul class="abs hero-list">
    <li>BETTER CONNECTIVITY</li><li>MORE CHOICE</li><li>LESS PAPER WORK</li><li>LOWER COSTS</li>
  </ul>
  <div class="abs btn btn-blue read-more">Read More</div>
  <span class="abs dot" style="left:186px"></span>
  <span class="abs dot" style="left:200px"></span>
  <span class="abs dot" style="left:213px;background:var(--green)"></span>
  <div class="abs video" role="img" aria-label="Promotional video player for Tendril Harbor, www.TendrilHarbor.co.uk">
    <svg width="356" height="199" viewBox="0 0 356 199">
      <rect x="338" y="4" width="15" height="12" rx="2" fill="#1d2733"/>
      <rect x="338" y="19" width="15" height="12" rx="2" fill="#1d2733"/>
      <rect x="338" y="34" width="15" height="12" rx="2" fill="#1d2733"/>
      <rect x="164" y="82" width="22" height="22" fill="#111"/>
      <path d="M171 87 L181 93 L171 99Z" fill="#fff"/>
      <rect x="2" y="183" width="352" height="14" rx="2" fill="#1d2733" opacity=".9"/>
      <rect x="4" y="184" width="24" height="12" rx="2" fill="#2c3a48"/>
      <path d="M13 187 L20 190 L13 193Z" fill="#fff"/>
      <rect x="34" y="189" width="272" height="2" fill="#556"/>
      <rect x="312" y="188" width="36" height="4" fill="#5c7d99"/>
    </svg>
  </div>
</section>

<section>
  <div class="abs features"></div>
  <div class="abs divider"></div>

  <div class="abs col-title" style="left:86px;top:489px">GP Locums</div>
  <div class="abs col-sub" style="left:86px;top:512px">The Complete platform to organise your locum life</div>
  <svg class="abs" style="left:88px;top:545px" width="36" height="36" viewBox="0 0 36 36"><circle cx="14" cy="14" r="10" fill="#cfe6f5" stroke="#556" stroke-width="3"/><path d="M21 21 L32 32" stroke="#333" stroke-width="5" stroke-linecap="round"/></svg>
  <div class="abs feat-title" style="left:129px;top:544px">Find Jobs</div>
  <div class="abs feat-desc" style="left:129px;top:559px">Search, apply and get invited for a wide selection of jobs from practises and agencies</div>
  <svg class="abs" style="left:92px;top:603px" width="36" height="32" viewBox="0 0 36 32"><rect x="1" y="1" width="34" height="23" rx="2" fill="#1d5f9a" stroke="#333" stroke-width="2"/><rect x="14" y="24" width="8" height="5" fill="#555"/><rect x="9" y="29" width="18" height="2" fill="#333"/></svg>
  <div class="abs feat-title" style="left:134px;top:602px">Do your locum admin easily online</div>
  <div class="abs feat-desc" style="left:134px;top:618px">Profile, diary management, invoicing, pension forms, finances, tax returns</div>
  <div class="abs icon-people" style="left:90px;top:664px" role="img" aria-label="Group of people around a globe"></div>
  <div class="abs feat-title" style="left:136px;top:660px">Create and grow your"employer network"</div>
  <div class="abs feat-desc" style="left:137px;top:676px;width:210px">Create your online profile and connect with your own network of employers allowing you to automatically fill jobs</div>
  <div class="abs btn btn-blue signup" style="left:143px;top:721px">Signup</div>

  <div class="abs col-title" style="left:422px;top:489px">Employers</div>
  <div class="abs col-sub" style="left:422px;top:512px">The Complete platform to organise your locum life</div>
  <svg class="abs" style="left:424px;top:545px" width="36" height="36" viewBox="0 0 36 36"><circle cx="14" cy="14" r="10" fill="#cfe6f5" stroke="#556" stroke-width="3"/><path d="M21 21 L32 32" stroke="#333" stroke-width="5" stroke-linecap="round"/></svg>
  <div class="abs feat-title" style="left:465px;top:544px">Find Locums</div>
  <div class="abs feat-desc" style="left:465px;top:559px">Search, apply and get invited for a wide selection of jobs from practises and agencies</div>
  <svg class="abs" style="left:428px;top:603px" width="36" height="32" viewBox="0 0 36 32"><rect x="1" y="1" width="34" height="23" rx="2" fill="#1d5f9a" stroke="#333" stroke-width="2"/><rect x="14" y="24" width="8" height="5" fill="#555"/><rect x="9" y="29" width="18" height="2" fill="#333"/></svg>
  <div class="abs feat-title" style="left:470px;top:602px">Do your locum admin easily online</div>
  <div class="abs feat-desc" style="left:471px;top:618px">Profile, diary management, invoicing, pension forms, finances, tax returns</div>
  <div class="abs icon-people" style="left:432px;top:662px;background:linear-gradient(#e8c9a8,#9db7cf)" role="img" aria-label="Two doctors"></div>
  <div class="abs feat-title" style="left:473px;top:660px">Create and grow your"Locum network"</div>
  <div class="abs feat-desc" style="left:474px;top:676px;width:210px">Create your online profile and connect with your own network of employers allowing you to automatically fill jobs</div>
  <div class="abs btn btn-green signup" style="left:479px;top:721px">Signup</div>
</section>

<section>
  <div class="abs trial"></div>
  <div class="abs trial-title">Try it now with just an email address, GMC number and password!</div>
  <div class="abs label" style="left:79px;top:833px">I am</div>
  <div class="abs label" style="left:108px;top:833px"><span class="radio"></span>a locum</div>
  <div class="abs label" style="left:178px;top:833px"><span class="radio"></span>an employer</div>
  <div class="abs label" style="left:79px;top:866px">Email :</div>
  <div class="abs field" style="top:864px"></div>
  <div class="abs label" style="left:79px;top:907px">Password :</div>
  <div class="abs field" style="top:903px"></div>
  <div class="abs label" style="left:79px;top:946px">GMC Number :</div>
  <div class="abs field" style="top:942px"></div>
  <div class="abs label" style="left:79px;top:987px">Password :</div>
  <div class="abs field" style="top:982px"></div>
  <div class="abs label" style="left:138px;top:1010px;font-size:7px"><span class="radio"></span>I agree to the terms of service and privacy policy</div>
  <div class="abs btn btn-green sign-up-big">SIGN UP</div>

  <div class="abs steps"></div>
  <div class="abs step-num" style="top:793px">1</div><div class="abs step-text" style="top:798px">The network for locums and employers</div>
  <div class="abs step-num" style="top:832px">2</div><div class="abs step-text" style="top:837px">Save time and cost</div>
  <div class="abs step-num" style="top:872px">3</div><div class="abs step-text" style="top:877px">Try it free now</div>

  <div class="abs press"></div>
  <div class="abs press-box" style="top:922px">Northgate Herald</div>
  <div class="abs press-box" style="top:964px">Evening Quill</div>
  <div class="abs press-box" style="top:1006px">Westmoor Times</div>
</section>

<footer>
  <div class="abs footer"></div>
  <div class="abs footer-title">Testimonials</div>
  <div class="abs avatar" style="left:72px" role="img" aria-label="Portrait of a smiling woman"></div>
  <div class="abs quote" style="left:143px">Nunc varius facilisis eros.<br>Sed erat. In in velit quis arcu<br>ornare laoreet. luctus&nbsp; massa<br>ornare laoreet. luctus&nbsp; massa.<br>Nunc varius facilisis eros.</div>
  <div class="abs person" style="left:143px">Ruth K.</div>
  <div class="abs avatar" style="left:279px;background:linear-gradient(#3a2d26,#b38a70)" role="img" aria-label="Portrait of a young man"></div>
  <div class="abs quote" style="left:350px">Nunc varius facilisis eros.<br>Sed erat. In in velit quis arcu<br>ornare laoreet. luctus&nbsp; massa<br>ornare laoreet. luctus&nbsp; massa.<br>Nunc varius facilisis eros.</div>
  <div class="abs person" style="left:350px">Oliver D.</div>
  <div class="abs more">MORE &gt;&gt;</div>
  <div class="abs social" style="left:611px;background:#3b5998"></div>
  <div class="abs social" style="left:636px;background:#2fa9e0"></div>
  <div class="abs social" style="left:660px;background:#1a75b5"></div>
  <div class="abs social" style="left:684px;background:#f08a1c"></div>
  <div class="abs copyright">© 2013 Tendril Harbor., All Rights Reserved</div>
</footer>
</body>
</html>
```